Hush and Cheer Gatherings Business Card Design

I provide event planning for surprise parties, celebrating all types of life events, such as birthdays, graduations, promotions, baby showers, bridal showers, grandparent showers, health (cancer survivor), wedding anniversary etc.

I would like to see designs that show that we are fun, creative, whimical, yet professional. I am not too fond of clip art, open to all shorts of fonts and graphics, especially photos of people that appear to be saying "shh" or people being surprised.

I am open to all colors, and was considering having the same logo/business card done in different color schemes that match the occasion/client such as bright colors for a birthday, silver, gold for anniversary, pastels for a baby related party or an older person's birthday.

I would like to have the word Surprise be very bold, and stick out from the rest of the lettering..almost like people are shouting "surprise" to the honoree.

Industry/Entity Type

Event Planning

Contact Information for Business Card

Hush and Cheer Gatherings!
T Harlow President/Owner
www.hushandcheerevents.com
tharlow@hushandcheerevents.com
555 318 2947
4173 Maple Hollow Rd
Brookmere Flats PA 19099

```html
<!DOCTYPE html>
<html lang="en">
<head>
<meta charset="utf-8">
<title>Hush and Cheer Gatherings – Business Card Options</title>
<link rel="stylesheet" href="https://fonts.googleapis.com/css2?family=Open+Sans:wght@400;600;700;800&display=swap">
<style>
  :root {
    --page: #ffffff;
    --label: #333333;
    --white: #ffffff;
    --plum: #8e1a86;
    --violet: #5b1f8e;
    --violet-text: #5a2590;
    --aqua-light: #effdfd;
    --aqua: #5ce0ea;
    --shadow: rgba(0, 0, 0, 0.28);
  }
  * { box-sizing: border-box; margin: 0; padding: 0; }
  html, body {
    width: 948px; height: 1200px; overflow: hidden;
    background: var(--page);
    font-family: "Open Sans", Arial, sans-serif;
  }
  .option-number {
    position: absolute; font-size: 36px; color: var(--label); font-weight: 400;
  }
  .card {
    position: absolute; overflow: hidden;
    box-shadow: 0 14px 18px -10px var(--shadow);
  }
  .icon { display: inline-block; vertical-align: middle; fill: none; stroke: currentColor; stroke-width: 1.6; }

  /* Option 1 */
  .card--rainbow {
    left: 86px; top: 67px; width: 797px; height: 475px; border-radius: 30px;
    background: linear-gradient(112deg, #2fd06b 0%, #33b1e6 13%, #f7e731 30%, #f59d1b 40%, #e6281f 51%, #c51c86 62%, #7a14b0 78%, #3d0d5e 100%);
  }
  .card--rainbow .portrait {
    position: absolute; left: 48px; top: 0; width: 250px; height: 334px;
    background: radial-gradient(ellipse at 50% 45%, #f3d2c0 0%, #e7b49b 35%, #c06a3e 70%, rgba(190,100,60,0) 100%);
  }
  .card--rainbow .star-trim {
    position: absolute; left: 0; top: 314px; width: 100%; height: 36px;
    background: linear-gradient(90deg, #35c7a0, #3fb6e0 25%, #b8e03a 50%, #f0a030 65%, #a0307a 85%, #5a1a70);
    opacity: 0.75;
  }
  .card--rainbow .title-band {
    position: absolute; left: 0; top: 334px; width: 100%; height: 141px;
    background: var(--plum);
    display: flex; align-items: center; justify-content: center;
  }
  .card--rainbow .brand-name {
    color: var(--white); font-size: 42px; font-weight: 700; letter-spacing: 0.5px;
  }
  .card--rainbow .contact {
    position: absolute; right: 40px; top: 62px; text-align: right; color: var(--white);
  }
  .card--rainbow .person { font-size: 22px; font-weight: 700; line-height: 28px; }
  .card--rainbow .role { font-size: 19px; line-height: 26px; margin-bottom: 10px; }
  .card--rainbow .line { font-size: 19px; line-height: 26px; }
  .card--rainbow .email { margin-bottom: 6px; }
  .card--rainbow .address { margin-bottom: 6px; }
  .card--rainbow .web { font-size: 20px; font-weight: 700; line-height: 30px; margin-bottom: 8px; }
  .card--rainbow .phone { font-size: 27px; font-weight: 700; line-height: 34px; }

  /* Option 2 */
  .card--aqua {
    left: 80px; top: 657px; width: 798px; height: 475px;
    background: radial-gradient(ellipse at 42% 45%, var(--aqua-light) 0%, #b9f3f6 45%, var(--aqua) 100%);
  }
  .card--aqua .title-band {
    position: absolute; left: 0; top: 0; width: 100%; height: 113px;
    background: var(--violet);
    display: flex; align-items: center; justify-content: center;
  }
  .card--aqua .brand-name {
    color: var(--white); font-size: 38px; font-weight: 800; letter-spacing: 0.5px;
  }
  .card--aqua .portrait {
    position: absolute; left: 280px; top: 113px; width: 518px; height: 299px;
    background: linear-gradient(90deg, rgba(160,95,50,0) 0%, rgba(160,95,50,0.55) 22%, rgba(200,150,120,0.7) 55%, #e9b89c 75%, #c46a35 100%);
  }
  .card--aqua .contact { position: absolute; left: 42px; top: 185px; color: var(--violet-text); }
  .card--aqua .person { font-size: 23px; font-weight: 700; line-height: 30px; }
  .card--aqua .role { font-size: 19px; line-height: 26px; margin-bottom: 14px; }
  .card--aqua .line { font-size: 19px; line-height: 25px; color: #2a2a3a; display: flex; gap: 8px; }
  .card--aqua .address { margin-bottom: 14px; }
  .card--aqua .bottom-band {
    position: absolute; left: 0; bottom: 0; width: 100%; height: 63px;
    background: var(--violet); color: var(--white);
    font-size: 23px; font-weight: 700;
  }
  .card--aqua .web { position: absolute; left: 86px; top: 15px; }
  .card--aqua .phone { position: absolute; left: 486px; top: 13px; font-size: 27px; }
</style>
</head>
<body>

<div class="option-number" style="left:28px; top:262px;">1</div>
<section class="card card--rainbow">
  <div class="portrait" role="img" aria-label="Photo of a surprised young girl with hands on her cheeks"></div>
  <div class="contact">
    <div class="person">T Harlow</div>
    <div class="role">President/Owner</div>
    <div class="line email">
      <svg class="icon" width="22" height="16" viewBox="0 0 22 16"><rect x="1" y="1" width="20" height="14"/><path d="M1 1l10 8 10-8"/></svg>
      tharlow@hushandcheerevents.com
    </div>
    <div class="line address">
      <svg class="icon" width="18" height="16" viewBox="0 0 18 16"><path d="M1 7L9 1l8 6M3 6v9h12V6M7 15v-5h4v5"/></svg>
      4173 Maple Hollow Rd<br>Brookmere Flats PA 19099
    </div>
    <div class="web">www.hushandcheerevents.com</div>
    <div class="phone">
      <svg class="icon" width="22" height="26" viewBox="0 0 22 26" style="stroke-width:2.4"><path d="M6 2l3 6-3 2c1 4 4 8 7 10l2-3 6 3-2 4c-8 0-17-11-17-19z"/></svg>
      555 318 2947
    </div>
  </div>
  <div class="star-trim" role="img" aria-label="Decorative row of colourful stars"></div>
  <div class="title-band">
    <div class="brand-name">Hush and Cheer Gatherings!</div>
  </div>
</section>

<div class="option-number" style="left:28px; top:892px;">2</div>
<section class="card card--aqua">
  <div class="title-band">
    <div class="brand-name">HUSH AND CHEER GATHERINGS!</div>
  </div>
  <div class="portrait" role="img" aria-label="Photo of a surprised red-haired girl with a flying braid"></div>
  <div class="contact">
    <div class="person">T Harlow</div>
    <div class="role">President/Owner</div>
    <div class="line address">
      <svg class="icon" width="20" height="18" viewBox="0 0 18 16" style="color:var(--violet-text)"><path d="M1 7L9 1l8 6M3 6v9h12V6M7 15v-5h4v5"/></svg>
      <span>4173 Maple Hollow Rd<br>Brookmere Flats PA 19099</span>
    </div>
    <div class="line">
      <svg class="icon" width="22" height="16" viewBox="0 0 22 16" style="color:var(--violet-text); margin-top:5px"><rect x="1" y="1" width="20" height="14"/><path d="M1 1l10 8 10-8"/></svg>
      tharlow@hushandcheerevents.com
    </div>
  </div>
  <div class="bottom-band">
    <div class="web">
      <svg class="icon" width="24" height="24" viewBox="0 0 24 24"><circle cx="12" cy="12" r="10"/><ellipse cx="12" cy="12" rx="4.5" ry="10"/><path d="M2 12h20M4 7h16M4 17h16"/></svg>
      www.hushandcheerevents.com
    </div>
    <div class="phone">
      <svg class="icon" width="22" height="26" viewBox="0 0 22 26" style="stroke-width:2.4"><path d="M6 2l3 6-3 2c1 4 4 8 7 10l2-3 6 3-2 4c-8 0-17-11-17-19z"/></svg>
      555 318 2947
    </div>
  </div>
</section>

</body>
</html>
```